Scientific project description

Here is a project description related to cellular mechanics, showing above the forces acting on cells in the tissues of our body. The forces on single cells are there to depict how forces are acting on cells (pressure squeezes the cell, shear flow is pushing the upward parts of the cell, tension pulls one part of the cell, strain is stretching the whole cell; the single cell images are to be found also on the last page). Intense red/purple are used to indicate that the forces are stressful (the colors to be used do not need to be exactly like these colors). The picture in the middle is a view of cells (same picture on next page if that needs to be modified). At the left, a description of what happens when everything is going well, i.e. the body stays healthy. At the right, if you dysfunction you get disease. Green nuances were used to indicate health, brownish, perhaps not so pleasant nuances were used to indicate disease. Below are the steps of the project.

On the whole, we're rather happy with the concept description as such, but it should look a little bit nicer. To many color nuances give a "noisy" impression, fonts could be nicer, layout more crisp, and the text on the steps should be more readable. We would also like to have two versions of the same picture, one with black background, one with white.

Target Market(s)

Scientists that are evaluating our project

Requirements
Must have
• Easy to grasp the idea, easy to read and understand the underlying idea.
Nice to have
• Would be good to have the Concept title ("Vorlint Concept and Envisioned Project Progression) on top of the figure as indicated in the second brief picture submitted.

```html
<!DOCTYPE html>
<html lang="en">
<head>
<meta charset="utf-8">
<title>Vorlint Concept and Envisioned Project Progression</title>
<link rel="stylesheet" href="https://fonts.googleapis.com/css2?family=Arimo:wght@400;700&display=swap">
<style>
  :root {
    --bg: #000000;
    --text: #ffffff;
    --muted: #c8c8c8;
    --force-red: #b00000;
    --force-wine: #8b0a30;
    --force-maroon: #7a0000;
    --force-purple: #7a1070;
    --health: #1db81d;
    --disease: #d4960a;
    --line: #8a8a8a;
  }
  * { margin: 0; padding: 0; box-sizing: border-box; }
  html, body { width: 1200px; height: 848px; overflow: hidden; background: var(--bg); }
  body { font-family: "Arimo", Arial, sans-serif; color: var(--text); }
  .canvas { position: relative; width: 1200px; height: 848px; overflow: hidden; background: var(--bg); }
  .backdrop {
    position: absolute; left: 0; top: 68px; width: 1200px; height: 780px;
    background: radial-gradient(ellipse at 50% 55%, #0d1a0c 0%, #071006 55%, #000 100%);
  }
  .artwork { position: absolute; left: 0; top: 0; }
  .title { position: absolute; left: 78px; top: 19px; font-size: 22px; font-weight: 700; }
  .legend-title { position: absolute; left: 131px; top: 134px; font-size: 18px; font-weight: 700; }
  .force-label { position: absolute; font-size: 16px; }
  .center-label { position: absolute; left: 337px; top: 566px; width: 266px; text-align: center; font-size: 28px; }
  .state { position: absolute; }
  .state h2 { font-size: 20px; font-weight: 700; }
  .state p { font-size: 16px; line-height: 22px; }
  .state.fitness { left: 118px; top: 541px; }
  .state.frailty { right: 367px; top: 537px; text-align: right; }
  .outcome { position: absolute; top: 637px; font-size: 28px; font-weight: 700; }
  .outcome.health { left: 119px; color: var(--health); }
  .outcome.disease { right: 367px; color: var(--disease); }
  .steps { position: absolute; left: 930px; top: 0; list-style: none; font-size: 26px; line-height: 34px; }
  .steps li { position: absolute; left: 0; white-space: nowrap; }
</style>
</head>
<body>
<div class="canvas">
  <div class="backdrop" role="img" aria-label="Faint fluorescence micrograph of cells in dark green tones"></div>

  <svg class="artwork" width="1200" height="848" viewBox="0 0 1200 848">
    <defs>
      <radialGradient id="cells" cx="50%" cy="50%" r="60%">
        <stop offset="0" stop-color="#2e5a22"/>
        <stop offset="0.6" stop-color="#1c3a16"/>
        <stop offset="1" stop-color="#3a1a14"/>
      </radialGradient>
      <radialGradient id="cells-faint" cx="50%" cy="50%" r="60%">
        <stop offset="0" stop-color="#1a3014"/>
        <stop offset="1" stop-color="#0a140a"/>
      </radialGradient>
      <marker id="head-red" viewBox="0 0 10 10" refX="8" refY="5" markerWidth="4" markerHeight="4" orient="auto">
        <path d="M0 0 L10 5 L0 10 Z" fill="#9a0d2a"/>
      </marker>
      <marker id="head-purple" viewBox="0 0 10 10" refX="8" refY="5" markerWidth="4" markerHeight="4" orient="auto">
        <path d="M0 0 L10 5 L0 10 Z" fill="#6e1466"/>
      </marker>
      <marker id="head-white" viewBox="0 0 10 10" refX="8" refY="5" markerWidth="5" markerHeight="5" orient="auto">
        <path d="M0 0 L10 5 L0 10" fill="none" stroke="#fff" stroke-width="2"/>
      </marker>
    </defs>

    <!-- legend swatches -->
    <g class="legend-swatches">
      <rect x="131" y="161" width="17" height="17" fill="var(--force-red)"/>
      <rect x="157" y="161" width="17" height="17" fill="var(--force-wine)"/>
      <rect x="182" y="161" width="17" height="17" fill="var(--force-maroon)"/>
      <rect x="207" y="161" width="17" height="17" fill="var(--force-purple)"/>
    </g>

    <!-- faint connector cell views -->
    <g class="connector-cells" opacity="0.45">
      <circle cx="398" cy="352" r="20" fill="url(#cells-faint)"/>
      <circle cx="555" cy="340" r="20" fill="url(#cells-faint)"/>
      <circle cx="252" cy="412" r="20" fill="url(#cells-faint)"/>
      <circle cx="288" cy="466" r="32" fill="url(#cells-faint)"/>
      <circle cx="412" cy="412" r="33" fill="url(#cells-faint)"/>
      <circle cx="533" cy="412" r="37" fill="url(#cells-faint)"/>
      <circle cx="678" cy="412" r="22" fill="url(#cells-faint)"/>
      <circle cx="638" cy="466" r="32" fill="url(#cells-faint)"/>
    </g>

    <!-- pressure -->
    <path role="img" aria-label="Cells under pressure, micrograph" d="M115 340 Q200 372 285 330 Q272 386 200 388 Q128 388 115 340 Z" fill="url(#cells)"/>
    <g stroke="#9a0d2a" stroke-width="3" marker-end="url(#head-red)">
      <line x1="130" y1="297" x2="130" y2="332"/>
      <line x1="162" y1="297" x2="162" y2="340"/>
      <line x1="193" y1="297" x2="193" y2="345"/>
      <line x1="225" y1="297" x2="225" y2="342"/>
      <line x1="257" y1="297" x2="257" y2="332"/>
    </g>

    <!-- shear -->
    <path role="img" aria-label="Cells under shear flow, micrograph" d="M318 318 Q425 302 472 238 Q490 262 478 292 Q452 330 330 330 Z" fill="url(#cells)"/>
    <g stroke="#9a0d2a" stroke-width="3" marker-end="url(#head-red)">
      <line x1="330" y1="283" x2="373" y2="283"/>
      <line x1="363" y1="267" x2="407" y2="267"/>
      <line x1="396" y1="248" x2="438" y2="248"/>
      <line x1="430" y1="230" x2="474" y2="230"/>
    </g>

    <!-- tension -->
    <path role="img" aria-label="Cells under tension, micrograph" d="M527 262 Q595 292 660 262 Q650 312 595 312 Q535 310 527 262 Z" fill="url(#cells)"/>
    <g stroke="#9a0d2a" stroke-width="3" marker-end="url(#head-red)">
      <line x1="562" y1="232" x2="562" y2="186"/>
      <line x1="598" y1="210" x2="598" y2="164"/>
      <line x1="633" y1="232" x2="633" y2="186"/>
    </g>

    <!-- strain -->
    <ellipse role="img" aria-label="Cells under strain, micrograph" cx="723" cy="362" rx="78" ry="24" fill="url(#cells)"/>
    <g stroke="#6e1466" stroke-width="3" marker-end="url(#head-purple)">
      <line x1="642" y1="348" x2="597" y2="348"/>
      <line x1="642" y1="368" x2="597" y2="368"/>
      <line x1="803" y1="348" x2="848" y2="348"/>
      <line x1="803" y1="368" x2="848" y2="368"/>
    </g>

    <!-- central view -->
    <circle role="img" aria-label="Fluorescence view of a cell population in mechanostasis" cx="470" cy="585" r="134" fill="url(#cells)"/>

    <!-- health / disease arrows -->
    <line x1="316" y1="580" x2="278" y2="580" stroke="#fff" stroke-width="3" marker-end="url(#head-white)"/>
    <g stroke="#fff" stroke-width="3">
      <line x1="622" y1="580" x2="656" y2="580"/>
      <line x1="623" y1="571" x2="623" y2="589"/>
    </g>

    <!-- project progression line -->
    <g class="progression">
      <line x1="905" y1="155" x2="905" y2="617" stroke="var(--line)" stroke-width="1.5"/>
      <g fill="#000" stroke="#d8d8d8" stroke-width="2">
        <circle cx="905" cy="187" r="8"/><circle cx="905" cy="240" r="8"/>
        <circle cx="905" cy="292" r="8"/><circle cx="905" cy="342" r="8"/>
        <circle cx="905" cy="393" r="8"/><circle cx="905" cy="444" r="8"/>
        <circle cx="905" cy="530" r="8"/>
      </g>
      <g fill="#d8d8d8">
        <circle cx="905" cy="187" r="4"/><circle cx="905" cy="240" r="4"/>
        <circle cx="905" cy="292" r="4"/><circle cx="905" cy="342" r="4"/>
        <circle cx="905" cy="393" r="4"/><circle cx="905" cy="444" r="4"/>
        <circle cx="905" cy="530" r="4"/>
      </g>
    </g>
  </svg>

  <h1 class="title">Vorlint Concept and Envisioned Project Progression</h1>
  <div class="legend-title">Forces on Cells</div>
  <div class="force-label" style="left:156px;top:274px">Pressure</div>
  <div class="force-label" style="left:332px;top:231px">Shear</div>
  <div class="force-label" style="left:566px;top:143px">Tension</div>
  <div class="force-label" style="left:701px;top:309px">Strain</div>

  <div class="center-label">Mechanostasis</div>

  <div class="state fitness">
    <h2>Cell Fitness</h2>
    <p>Functional cellular<br>machineries</p>
  </div>
  <div class="state frailty">
    <h2>Cell Frailty</h2>
    <p>Dysfunctional cellular<br>machineries</p>
  </div>
  <div class="outcome health">Health</div>
  <div class="outcome disease">Disease</div>

  <ol class="steps">
    <li style="top:171px">Therapies</li>
    <li style="top:223px">Prevention</li>
    <li style="top:274px">Critical Targets</li>
    <li style="top:325px">Cellular Machineries</li>
    <li style="top:376px">Disease Models</li>
    <li style="top:428px">Cell, Tissue and<br>Organ Responses</li>
    <li style="top:513px">Mechanical Force<br>Models</li>
  </ol>
</div>
</body>
</html>
```